TR Advisory Business Cards - High End AV / Low Voltage Company

We are low voltage AV company that specializes in high end clients on the residential side and larger businesses on the commercial side. We want something modern, tech looking but also something that is extremely professional looking. We have uploaded our logos and postcards we already have in the field. Along with a picture of one of our wrapped vans. Our website is at www.trvadvisory.example and our primary colors are the orange, green, grey and blue all military color finishes.

We are interesting in the slogans "Pairing You with the Right Technology" or "Leading the Lowcountry in Tech"

Target Market(s)

We focus on 70% Commercial and 30% Residential Customers

Industry/Entity Type

Low Voltage, AV Company

Contact Information for Business Card

Name - Dorian Fairweather, Title - Owner, Office Phone - 555-714-3096, Mobile Phone - 555-802-4173, E-Mail - d@trvadvisory.example, Website: www.trvadvisory.example

Font styles to use
Sans Serif

Requirements
Must have
• Must have Name, Title, Work Phone & Mobile, Website and Logo.
Nice to have
• We want something that will impress our higher end clients with a great logo
Should not have
• Too traditional or plain.

```html
<!DOCTYPE html>
<html lang="en">
<head>
<meta charset="utf-8">
<title>TR Advisory — Business Cards</title>
<link href="https://fonts.googleapis.com/css2?family=Montserrat:wght@400;600;700&display=swap" rel="stylesheet">
<style>
  :root {
    --brand-orange: #ee6a3a;
    --brand-grey: #848589;
    --ink: #141414;
    --paper: #ffffff;
    --backdrop: #4a3f38;
  }
  * { margin: 0; padding: 0; box-sizing: border-box; }
  html, body { width: 1200px; height: 1200px; overflow: hidden; }
  body {
    background: var(--backdrop);
    font-family: "Montserrat", Arial, sans-serif;
    position: relative;
  }
  .card {
    position: absolute;
    left: 260px;
    width: 680px;
    height: 440px;
    overflow: hidden;
  }
  .card--front { top: 130px; background: var(--paper); }
  .card--back { top: 630px; background: var(--brand-orange); }

  .brand {
    position: absolute;
    display: flex;
    flex-direction: column;
    align-items: center;
  }
  .brand__ring {
    width: 110px; height: 110px;
    border-radius: 50%;
    border: 6px solid currentColor;
  }
  .brand__name {
    margin-top: 14px;
    font-weight: 700;
    font-size: 21px;
    letter-spacing: 1.5px;
    white-space: nowrap;
  }
  .card--front .brand { left: 460px; top: 26px; width: 200px; color: var(--brand-orange); }
  .card--back .brand { left: 240px; top: 134px; width: 200px; color: var(--paper); }
  .card--back .brand__ring { width: 124px; height: 124px; }
  .card--back .brand__name { font-size: 23px; }

  .person { position: absolute; left: 52px; top: 186px; color: var(--ink); }
  .person__name { font-weight: 600; font-size: 24px; line-height: 1; }
  .person__title { font-weight: 400; font-size: 14px; margin-top: 5px; letter-spacing: 0.3px; }

  .contacts { position: absolute; left: 52px; top: 250px; list-style: none; }
  .contacts__item {
    display: flex; align-items: center;
    height: 31px; margin-bottom: 13.5px;
    font-size: 17px; color: var(--ink); letter-spacing: 0.4px;
  }
  .contacts__icon {
    width: 31px; height: 31px; border-radius: 50%;
    background: var(--brand-orange);
    display: flex; align-items: center; justify-content: center;
    margin-right: 12px; flex: none;
  }
  .contacts__icon svg { width: 18px; height: 18px; }

  .footer-band { position: absolute; left: 0; bottom: 0; width: 680px; height: 43px; }
  .footer-band svg { position: absolute; inset: 0; }
  .footer-band__url {
    position: absolute; left: 0; width: 476px; top: 11px;
    text-align: center; color: var(--paper);
    font-size: 17px; letter-spacing: 0.5px;
  }
</style>
</head>
<body>

<section class="card card--front" aria-label="Business card front">
  <div class="brand">
    <div class="brand__ring"></div>
    <div class="brand__name">TR Advisory</div>
  </div>

  <div class="person">
    <p class="person__name">Dorian Fairweather</p>
    <p class="person__title">Owner</p>
  </div>

  <ul class="contacts">
    <li class="contacts__item">
      <span class="contacts__icon">
        <svg viewBox="0 0 24 24"><path fill="#fff" d="M15 4.5c-3.2.8-5 3.9-5 7.5s1.8 6.7 5 7.5l1-3.2c-1.6-.5-2.5-2.2-2.5-4.3s.9-3.8 2.5-4.3z"/></svg>
      </span>
      555-714-3096
    </li>
    <li class="contacts__item">
      <span class="contacts__icon">
        <svg viewBox="0 0 24 24"><rect x="7" y="3" width="10" height="18" rx="1.5" fill="none" stroke="#fff" stroke-width="1.8"/><circle cx="12" cy="18" r="1" fill="#fff"/></svg>
      </span>
      555-802-4173
    </li>
    <li class="contacts__item">
      <span class="contacts__icon">
        <svg viewBox="0 0 24 24"><rect x="2.5" y="6" width="19" height="12.5" fill="none" stroke="#fff" stroke-width="1.5"/><path d="M2.5 6l9.5 7 9.5-7M2.5 18.5l7-6M21.5 18.5l-7-6" fill="none" stroke="#fff" stroke-width="1.3"/></svg>
      </span>
      d@trvadvisory.example
    </li>
  </ul>

  <div class="footer-band">
    <svg width="680" height="43" viewBox="0 0 680 43">
      <polygon points="0,0 475,0 431,43 0,43" fill="var(--brand-orange)"/>
      <polygon points="501,0 680,0 680,43 458,43" fill="var(--brand-grey)"/>
    </svg>
    <p class="footer-band__url">www.trvadvisory.example</p>
  </div>
</section>

<section class="card card--back" aria-label="Business card back">
  <div class="brand">
    <div class="brand__ring"></div>
    <div class="brand__name">TR Advisory</div>
  </div>
</section>

</body>
</html>
```